Zentrova - Creative Automation

We are a software house for Audio Visual Systems integration/automation and home automation. we develop innovative software to automate a variety of devices mainly related to audio visuals and we design touch panel user interfaces to control these systems.

We would like to see designs that stick to our colours and theme, which you can find on our webpage www.zentrova.com.au

The final design should communicate touch panels, innovation, software and automation.

Industry/Entity Type

Software

Requirements
Must have
• The business card must show the following information:
Name example : Derek Malloway
Qualification example: B Eng ICT(CompSys) Dip EngPrac
Title example : Control Systems Programmer
Mobile Phone, Company phone, Email address ,Company website

```html
<!DOCTYPE html>
<html lang="en">
<head>
<meta charset="utf-8">
<title>Zentrova – Business Card</title>
<link rel="stylesheet" href="https://fonts.googleapis.com/css2?family=Oswald:wght@300;400;500&display=swap">
<style>
  :root {
    --brand-blue: #1b75bc;
    --brand-green: #1fa463;
    --ink: #1a1a1a;
    --back-black: #050a0b;
    --trace-tint: #0c2419;
    --paper: #ffffff;
    --rule: #3a3a3a;
    --carbon-dark: #0b0b0b;
    --carbon-mid: #3a3a3a;
  }
  * { margin: 0; padding: 0; box-sizing: border-box; }
  html, body {
    width: 895px; height: 1200px; overflow: hidden;
    background: var(--back-black);
    font-family: "Oswald", "Arial Narrow", sans-serif;
  }
  .canvas { position: relative; width: 895px; height: 1200px; }

  /* Front side */
  .card-front {
    position: absolute; left: 0; top: 0; width: 895px; height: 596px;
    background: radial-gradient(ellipse 60% 55% at 50% 42%, var(--carbon-mid) 0%, #1d1d1d 50%, var(--carbon-dark) 100%);
  }
  .front-texture { position: absolute; inset: 0; }
  .front-brand {
    position: absolute; inset: 0;
    display: flex; align-items: center; justify-content: center;
  }
  .front-lockup { position: relative; display: flex; align-items: center; gap: 22px; margin-top: -24px; }
  .brand-square { width: 78px; height: 78px; background: var(--brand-blue); }
  .brand-name {
    font-size: 92px; font-weight: 400; line-height: 1; color: var(--paper);
    letter-spacing: 1px;
  }
  .brand-tagline {
    position: absolute; right: 4px; bottom: -22px;
    font-size: 15px; font-weight: 400; color: var(--paper); letter-spacing: 0.5px;
  }

  /* Back side */
  .card-back {
    position: absolute; left: 0; top: 599px; width: 895px; height: 601px;
    background: var(--back-black);
  }
  .trace-area {
    position: absolute; left: 30px; top: 0; width: 110px; height: 568px;
    background: linear-gradient(180deg, var(--back-black) 0%, var(--trace-tint) 100%);
  }

  .contact-panel {
    position: absolute; left: 555px; top: 0; width: 292px; height: 552px;
    background: var(--paper);
  }
  .panel-brand {
    position: absolute; left: 0; right: 0; top: 170px;
    text-align: center; font-size: 40px; font-weight: 400; color: var(--brand-blue);
  }
  .person-name {
    position: absolute; right: 7px; top: 308px;
    font-size: 42px; font-weight: 400; color: var(--brand-blue); line-height: 1;
    letter-spacing: -0.5px; white-space: nowrap;
  }
  .person-qualification {
    position: absolute; right: 7px; top: 364px;
    font-size: 18px; font-weight: 400; color: var(--brand-green); line-height: 1;
    white-space: nowrap;
  }
  .divider {
    position: absolute; left: 7px; right: 7px; top: 398px;
    height: 2px; background: var(--rule);
  }
  .person-title {
    position: absolute; right: 7px; top: 412px;
    font-size: 26px; font-weight: 400; color: var(--ink); line-height: 1;
    letter-spacing: -0.3px; white-space: nowrap;
  }
  .contact-list {
    position: absolute; right: 7px; top: 453px;
    list-style: none; font-size: 18px; font-weight: 300; color: var(--ink);
    text-align: right; white-space: nowrap;
  }
  .contact-list li { line-height: 24px; }
  .contact-list .contact-email { line-height: 28px; }
  .contact-list .contact-web { line-height: 20px; }
</style>
</head>
<body>
<div class="canvas">

  <section class="card-front">
    <div class="front-texture" role="img" aria-label="Dark carbon fibre texture background"></div>
    <div class="front-brand">
      <div class="front-lockup">
        <div class="brand-square"></div>
        <div class="brand-name">Zentrova</div>
        <div class="brand-tagline">Creative Automation</div>
      </div>
    </div>
  </section>

  <section class="card-back">
    <div class="trace-area" role="img" aria-label="Decorative green circuit trace ending in a ringed connector"></div>

    <div class="contact-panel">
      <div class="panel-brand">Zentrova</div>
      <h1 class="person-name">Derek Malloway</h1>
      <p class="person-qualification">B Eng ICT(CompSys) Dip EngPrac</p>
      <div class="divider"></div>
      <h2 class="person-title">Control Systems Programmer</h2>
      <ul class="contact-list">
        <li class="contact-mobile">0412 558 904</li>
        <li class="contact-office">0247 553 180</li>
        <li class="contact-email">support@zentrova.com.au</li>
        <li class="contact-web">zentrova.com.au</li>
      </ul>
    </div>
  </section>

</div>
</body>
</html>
```